Business Card Design

This is a new business to be run from my home. I have attended certificate workshops run by Dr Kevin Ruddock who is a Master Trainer in Gentle Flow for Mobility.
I wish to communicate to people that Tai Chi is for everyone, no matter their age, gender or fitness levels. Tai Chi is taught both standing & seated.
The card should have a slightly Asian feel, mainly printed in black & white with perhaps a little soft pink &/or green.

Target Market(s)

people of all ages from 10 years up, poor fitness & mild disabilities.

Industry/Entity Type

Fitness

Contact Information for Business Card

Marrowdene Flowing Arts for Body, Mind & Stillness

Brenna Holcroft, Certificated Leader

ph 5281 9046

Requirements
Nice to have
• a feeling of health & peace.
Should not have
• bright colours, fancy fonts

```html
<!DOCTYPE html>
<html lang="en">
<head>
<meta charset="utf-8">
<title>Marrowdene Flowing Arts – Business Card</title>
<link rel="stylesheet" href="https://fonts.googleapis.com/css2?family=Anton&family=Open+Sans:wght@700&family=Varela+Round&display=swap">
<style>
  :root {
    --backdrop: #d9d9d9;
    --card: #ffffff;
    --ink: #0c0c0c;
    --green: #3b9a48;
    --haze: #e4e4e4;
    --art-light: #f2f2f2;
    --art-dark: #9a9a9a;
  }
  * { margin: 0; padding: 0; box-sizing: border-box; }
  html, body {
    width: 1200px; height: 900px; overflow: hidden;
    background: var(--backdrop);
  }
  .card {
    position: absolute; left: 80px; top: 130px;
    width: 1040px; height: 640px;
    background: radial-gradient(ellipse 70% 80% at 62% 45%, var(--card) 0%, var(--card) 25%, var(--haze) 100%);
    overflow: hidden;
  }
  .card__title {
    position: absolute; left: 0; right: 0; top: 62px;
    text-align: center;
    font-family: "Anton", Impact, sans-serif;
    font-size: 50px; letter-spacing: 1px; line-height: 1;
    color: var(--ink);
  }
  .card__tagline {
    position: absolute; left: 0; width: 880px; top: 128px;
    text-align: center;
    font-family: "Open Sans", Arial, sans-serif; font-weight: 700;
    font-size: 30px; color: var(--green);
  }
  .card__art {
    position: absolute; left: 630px; top: 125px;
    width: 375px; height: 430px;
    background: radial-gradient(ellipse at 45% 50%, var(--art-dark) 0%, var(--art-light) 75%, transparent 100%);
  }
  .holder {
    position: absolute; left: 69px; top: 340px;
    font-family: "Varela Round", Arial, sans-serif;
  }
  .holder__name { font-size: 33px; color: var(--green); line-height: 1.15; }
  .holder__role { font-size: 23px; color: var(--ink); margin-top: 4px; }
  .contact {
    position: absolute; left: 69px; top: 478px;
    display: flex; align-items: center; gap: 14px;
    font-family: "Varela Round", Arial, sans-serif;
    font-size: 37px; color: var(--ink);
  }
  .contact__icon { width: 34px; height: 34px; fill: var(--green); }
  .card__rule {
    position: absolute; left: 0; right: 0; top: 564px;
    height: 6px; background: var(--green);
  }
  .card__band {
    position: absolute; left: 0; right: 0; top: 576px; bottom: 0;
    background: var(--ink);
  }
</style>
</head>
<body>
  <div class="card">
    <h1 class="card__title">MARROWDENE FLOWING ARTS FOR BODY</h1>
    <p class="card__tagline">Mind &amp; Stillness</p>

    <div class="card__art" role="img" aria-label="Black ink illustration of a coiling Chinese dragon beside a yin-yang symbol"></div>

    <div class="holder">
      <p class="holder__name">Brenna Holcroft</p>
      <p class="holder__role">Certificated Leader</p>
    </div>

    <p class="contact">
      <svg class="contact__icon" viewBox="0 0 24 24" aria-hidden="true">
        <path d="M6.6 10.8c1.4 2.8 3.8 5.1 6.6 6.6l2.2-2.2c.3-.3.7-.4 1-.2 1.1.4 2.3.6 3.6.6.6 0 1 .4 1 1V20c0 .6-.4 1-1 1C10.6 21 3 13.4 3 4c0-.6.4-1 1-1h3.5c.6 0 1 .4 1 1 0 1.3.2 2.5.6 3.6.1.3 0 .7-.2 1l-2.3 2.2z"/>
      </svg>
      <span>5281 9046</span>
    </p>

    <div class="card__rule"></div>
    <div class="card__band"></div>
  </div>
</body>
</html>
```